infographic

Infographic to be posted on chatterloop, website and shared by email very simply illustrating the below:

Meridian has doubled access to paid parental leave:
• Only about 50 per cent of working women had access to paid maternity leave before the Government introduced its scheme on 1 January 2011.
• Today 95 per cent of working women have access to paid parental leave (18 weeks at minimum wage)

Target Market(s)

women aged 30-45 with kids

Industry/Entity Type

Government

Requirements
Must have
• please use red for the 95% and blue for the 50% (red is meridian's colour)

```html
<!DOCTYPE html>
<html lang="en">
<head>
<meta charset="utf-8">
<title>Meridian has doubled access to paid parental leave</title>
<link rel="stylesheet" href="https://fonts.googleapis.com/css2?family=Parisienne&family=Open+Sans:ital,wght@1,800&display=swap">
<style>
  :root {
    --heading-blue: #1d5fa8;
    --bullet-blue: #2a7fc8;
    --stat-blue: #1f63b5;
    --meridian-red: #e3161d;
    --deep-red: #c8141b;
    --soft-red: #f6c3c3;
    --paper: #ffffff;
    --mist: #d9d9db;
  }
  * { margin: 0; padding: 0; box-sizing: border-box; }
  html, body { width: 1200px; height: 848px; overflow: hidden; background: var(--paper); }
  .infographic {
    position: relative;
    width: 1200px;
    height: 848px;
    overflow: hidden;
    background: radial-gradient(ellipse 70% 80% at 30% 45%, #ffffff 0%, #f3f3f4 55%, var(--mist) 100%);
  }
  .portrait {
    position: absolute;
    right: 0;
    top: 0;
    width: 420px;
    height: 848px;
    background:
      radial-gradient(ellipse 48% 40% at 62% 52%, #111111 0%, #161616 60%, rgba(22,22,22,0) 100%),
      linear-gradient(90deg, rgba(235,235,236,0) 0%, rgba(150,150,152,0.6) 30%, #3a3a3a 62%, #1a1a1a 100%);
  }
  .headline {
    position: absolute;
    left: 34px;
    top: 22px;
    font-family: "Parisienne", cursive;
    font-weight: 400;
    font-size: 70px;
    line-height: 82px;
    color: var(--paper);
    -webkit-text-stroke: 1.6px var(--heading-blue);
    letter-spacing: 1px;
    white-space: nowrap;
  }
  .facts {
    position: absolute;
    left: 30px;
    top: 220px;
    list-style: none;
  }
  .fact {
    position: relative;
    padding-left: 41px;
    font-family: "Open Sans", sans-serif;
    font-style: italic;
    font-weight: 800;
    font-size: 38px;
    line-height: 53px;
    color: var(--meridian-red);
    white-space: nowrap;
  }
  .fact + .fact { margin-top: 37px; }
  .stat-before { color: var(--stat-blue); }
  .stat-now { color: var(--meridian-red); }
  .fact-marker {
    position: absolute;
    left: 0;
    top: 15px;
    width: 26px;
    height: 24px;
  }
  .wave {
    position: absolute;
    left: 0;
    top: 0;
    width: 1200px;
    height: 848px;
  }
</style>
</head>
<body>
<main class="infographic">
  <div class="portrait" role="img" aria-label="Silhouette of a pregnant woman holding her belly, dark against a soft grey backdrop"></div>

  <svg class="wave" viewBox="0 0 1200 848" aria-hidden="true">
    <defs>
      <radialGradient id="red-glow" cx="42%" cy="88%" r="60%">
        <stop offset="0" stop-color="#fbe3e3"/>
        <stop offset="0.3" stop-color="#f6c3c3"/>
        <stop offset="0.7" stop-color="#e3161d"/>
        <stop offset="1" stop-color="#c8141b"/>
      </radialGradient>
      <linearGradient id="blue-fade" x1="0" x2="1" y1="0" y2="0">
        <stop offset="0" stop-color="#1d5fa8"/>
        <stop offset="0.45" stop-color="#7fb3e4"/>
        <stop offset="0.75" stop-color="#ffffff" stop-opacity="0"/>
      </linearGradient>
    </defs>
    <path d="M0,668 C250,735 620,720 1200,560 L1200,848 L0,848 Z" fill="url(#red-glow)"/>
    <path d="M0,668 C250,735 620,720 1200,560" fill="none" stroke="url(#blue-fade)" stroke-width="9"/>
  </svg>

  <h1 class="headline">Meridian has doubled access to<br>paid parental leave:</h1>

  <ul class="facts">
    <li class="fact">
      <svg class="fact-marker" viewBox="0 0 26 24" aria-hidden="true">
        <circle cx="13" cy="12" r="11" fill="#2a7fc8"/>
        <circle cx="13" cy="12" r="4" fill="#ffffff"/>
      </svg>
      Only about <span class="stat-before">50 percent</span> of working women<br>had access to paid maternity leave before<br>the Government introduced its scheme<br>on 1 January 2011.
    </li>
    <li class="fact">
      <svg class="fact-marker" viewBox="0 0 26 24" aria-hidden="true">
        <circle cx="13" cy="12" r="11" fill="#2a7fc8"/>
        <circle cx="13" cy="12" r="4" fill="#ffffff"/>
      </svg>
      Today <span class="stat-now">95 percent</span> of working women have<br>access to paid parental leave<br>(18 weeks at minimum wage)
    </li>
  </ul>
</main>
</body>
</html>
```